Speisekarten-Design für italienisches Restaurant im Golfclub mit Blick auf die Alpen
Zielgruppe
Italienisches Restaurant im Golfclub mit Blick auf die Alpen (bei gutem Wetter)
Aufgabenstellung
Karte muss weiterhin bearbeitet werden könne. Es geht um ein Design das optisch anspricht aber nicht übertrieben ist. Die Blätter kommen später in eine Menukarte die noch in Auftrag gegeben werden.
Im Idealfall kann der Designer hierfür auch was mit designen das an einen Firma weitergeben werden kann um die 'Umschläge zu erstellen. Logo kann muss nicht mit drin sein. Es geht auch sehr um die einfache Darstellung des Ganzen.

```html
<!DOCTYPE html>
<html lang="de">
<head>
<meta charset="utf-8">
<title>Speisekarte – Ristorante Vallombra</title>
<link rel="stylesheet" href="https://fonts.googleapis.com/css2?family=Oswald:wght@500;600&family=Archivo:wght@400&family=Cinzel:wght@600&display=swap">
<style>
  :root {
    --header-bg: #231f20;
    --paper: #f0ebe2;
    --sketch: #f7f4ef;
    --ink: #444243;
    --gold: #c9a04c;
  }
  * { margin: 0; padding: 0; box-sizing: border-box; }
  html, body { width: 735px; height: 1200px; overflow: hidden; }
  body { background: var(--paper); position: relative; font-family: "Archivo", sans-serif; color: var(--ink); }

  .masthead {
    position: absolute; left: 0; top: 0; width: 735px; height: 180px;
    background: var(--header-bg);
    display: flex; align-items: center; justify-content: center;
  }
  .brand-name {
    font-family: "Cinzel", serif; font-weight: 600; font-size: 30px;
    letter-spacing: 3px; color: var(--gold);
  }

  .sketch-seafood, .sketch-pasta {
    position: absolute; background: var(--sketch); opacity: .75;
  }
  .sketch-seafood { left: 270px; top: 205px; width: 400px; height: 520px; border-radius: 48% 40% 46% 44%; }
  .sketch-pasta { left: 150px; top: 730px; width: 510px; height: 450px; border-radius: 44% 50% 40% 48%; }

  .menu-section { position: absolute; left: 121px; width: 518px; }
  .section-vorspeisen { top: 250px; }
  .section-pasta { top: 696px; }
  .section-title {
    font-family: "Oswald", sans-serif; font-weight: 600; font-size: 50px;
    line-height: 1; letter-spacing: -0.5px; color: var(--ink); margin-bottom: 28px;
  }
  .dish-list { list-style: none; }
  .dish {
    display: flex; justify-content: space-between; align-items: baseline;
    height: 31.7px;
  }
  .dish-name { font-size: 13.3px; }
  .dish-price { font-family: "Oswald", sans-serif; font-weight: 500; font-size: 19px; width: 28px; }
</style>
</head>
<body>
  <header class="masthead">
    <span class="brand-name">RISTORANTE VALLOMBRA</span>
  </header>

  <div class="sketch-seafood" role="img" aria-label="Helle Strichzeichnung zweier Flusskrebse als Hintergrunddekor"></div>
  <div class="sketch-pasta" role="img" aria-label="Helle Strichzeichnung von Pasta, Basilikumblättern und Tomatenscheibe als Hintergrunddekor"></div>

  <section class="menu-section section-vorspeisen">
    <h2 class="section-title">VORSPEISEN</h2>
    <ul class="dish-list">
      <li class="dish"><span class="dish-name">Vorspeise Teller nach Art des Hauses</span><span class="dish-price">12,-</span></li>
      <li class="dish"><span class="dish-name">Meeresfrüchte Vorspeise</span><span class="dish-price">14,-</span></li>
      <li class="dish"><span class="dish-name">Aufschnitt und Meeresfrüchte Vorspeise</span><span class="dish-price">14,-</span></li>
      <li class="dish"><span class="dish-name">Rinder Carpaccio</span><span class="dish-price">12,-</span></li>
      <li class="dish"><span class="dish-name">Gemischter Salat</span><span class="dish-price">5,-</span></li>
      <li class="dish"><span class="dish-name">Vitello Tonnato</span><span class="dish-price">12,-</span></li>
      <li class="dish"><span class="dish-name">Bruschetta 2 Stück</span><span class="dish-price">4,-</span></li>
      <li class="dish"><span class="dish-name">Gemüse Vorspeise</span><span class="dish-price">10,-</span></li>
      <li class="dish"><span class="dish-name">Crevetten Cochtail</span><span class="dish-price">11,-</span></li>
    </ul>
  </section>

  <section class="menu-section section-pasta">
    <h2 class="section-title">PASTA</h2>
    <ul class="dish-list">
      <li class="dish"><span class="dish-name">Lasagne im Ofen überbacken</span><span class="dish-price">12,-</span></li>
      <li class="dish"><span class="dish-name">Paccheri mit Hackfleischsoße</span><span class="dish-price">12,-</span></li>
      <li class="dish"><span class="dish-name">Ravioli mit Ricotta- und Spinatfüllung</span><span class="dish-price">13,-</span></li>
      <li class="dish"><span class="dish-name">Risotto mit Steinpilzsoße</span><span class="dish-price">13,-</span></li>
      <li class="dish"><span class="dish-name">Gnocchi mit Tomatensoße und Mozzarella</span><span class="dish-price">12,-</span></li>
      <li class="dish"><span class="dish-name">Tortellini mit Rahmsoße</span><span class="dish-price">12,-</span></li>
      <li class="dish"><span class="dish-name">Zweierlei Pasta</span><span class="dish-price">13,-</span></li>
      <li class="dish"><span class="dish-name">Orecchiette mit Gemüse</span><span class="dish-price">12,-</span></li>
    </ul>
  </section>
</body>
</html>
```